Inspiration Poster

Inspirational Poster that has a Kamran Dulo like abstract look (http://www.vexalo.com/images/search?q=kamran+dulo&FORM=HDRSC2) with the text:

"we walk not in order to arrive at the promise land but because walking itself is a revolution"
-Peter Ambrick

```html
<!DOCTYPE html>
<html lang="en">
<head>
<meta charset="utf-8">
<title>Inspiration Poster</title>
<link rel="stylesheet" href="https://fonts.googleapis.com/css2?family=Ribeye&display=swap">
<style>
  :root {
    --ink-red: #6e1119;
    --cream: #ebe8d3;
    --mist: #c9cccb;
    --sand-grey: #a9abae;
    --deep-red: #6a0d16;
  }
  html, body {
    margin: 0;
    padding: 0;
    width: 1200px;
    height: 921px;
    overflow: hidden;
    background: var(--cream);
  }
  .poster {
    position: relative;
    width: 1200px;
    height: 921px;
    overflow: hidden;
  }
  .beach-scene {
    position: absolute;
    inset: 0;
    background:
      radial-gradient(ellipse 70% 60% at 100% 100%, var(--deep-red) 0%, rgba(106,13,22,0.75) 35%, rgba(106,13,22,0) 75%),
      radial-gradient(ellipse 45% 40% at 0% 100%, rgba(106,13,22,0.7) 0%, rgba(106,13,22,0) 70%),
      linear-gradient(180deg, var(--cream) 0%, var(--mist) 40%, var(--sand-grey) 70%, #9a8d90 100%);
  }
  .quote {
    position: absolute;
    left: 507px;
    top: 96px;
    margin: 0;
    font-family: "Ribeye", cursive;
    font-size: 42px;
    line-height: 76px;
    color: var(--ink-red);
    font-weight: 400;
  }
  .quote span { display: block; white-space: nowrap; }
  .quote .indent { padding-left: 12px; }
  .attribution {
    position: absolute;
    left: 507px;
    top: 462px;
    margin: 0;
    font-family: "Ribeye", cursive;
    font-size: 42px;
    color: var(--ink-red);
  }
</style>
</head>
<body>
  <main class="poster">
    <div class="beach-scene" role="img" aria-label="Photo of bare feet walking away across wet sand, leaving a trail of footprints, toned in cream and dark red"></div>
    <p class="quote">
      <span>"we walk not in order to</span>
      <span>arrive at the promise land</span>
      <span class="indent">but because walking itself</span>
      <span class="indent">is a revolution"</span>
    </p>
    <p class="attribution">-Peter Ambrick</p>
  </main>
</body>
</html>
```